Business card design needed

We are a boutique law firm within the Melbourne CBD.

You will need to upload our company logo which is to go on the left hand side of the business card - we then have a Legal Guild of Carrowmere logo to go perhaps on the bottom right hand side (color)

On the back we would like the website details

www.hartwellsolicitors.com.au - with a small logo
Updates

Thank you designers for all your great submissions.  Just going through the designs and we will choose one within the next couple of days.

Kind Regards
Hartwells Solicitors Pty Ltd

Industry/Entity Type

Boutique

Contact Information for Business Card

Dominic Hartwell
Principal
Level 6, 47 Penrose Street
Melbourne VIC Australia 3000
T+61 3 9555 0142 F+61 3 9555 0187
dominic@hartwellsolicitors.com.au
M 0491 570 156

```html
<!DOCTYPE html>
<html lang="en">
<head>
<meta charset="utf-8">
<title>Hartwells Solicitors – Business Card</title>
<link rel="stylesheet" href="https://fonts.googleapis.com/css2?family=Source+Sans+3:wght@400;700&display=swap">
<style>
  :root {
    --page: #ffffff;
    --ink: #000000;
    --cream: #f0e9c8;
    --text: #1f1f1f;
    --shadow-mark: #2b2b2b;
    --gold-soft: #e6d9a4;
  }
  html, body {
    margin: 0;
    width: 1200px;
    height: 741px;
    overflow: hidden;
    background: var(--page);
  }
  .card {
    position: absolute;
    left: 37px;
    top: 49px;
    width: 1135px;
    height: 647px;
    background: var(--cream);
    overflow: hidden;
    font-family: "Source Sans 3", "Myriad Pro", Arial, sans-serif;
  }
  .header-band {
    position: absolute;
    left: 0; top: 0;
    width: 100%; height: 209px;
    background: var(--ink);
  }
  .footer-band {
    position: absolute;
    left: 0; bottom: 0;
    width: 100%; height: 28px;
    background: var(--ink);
  }
  .brand-mark {
    position: absolute;
    left: 72px; top: 40px;
    width: 150px; height: 150px;
    background: var(--cream);
  }
  .brand-name {
    position: absolute;
    margin: 0;
    font-weight: 700;
    font-size: 84px;
    line-height: 1;
    letter-spacing: -1px;
  }
  .brand-name--primary {
    left: 250px; top: 105px;
    color: var(--cream);
  }
  .brand-name--echo {
    left: 760px; top: 105px;
    color: var(--shadow-mark);
  }
  .scales-small {
    position: absolute;
    left: 898px; top: 22px;
    width: 180px; height: 100px;
    background: var(--shadow-mark);
    opacity: 0.6;
  }
  .scales-large {
    position: absolute;
    left: 800px; top: 225px;
    width: 320px; height: 390px;
    background: radial-gradient(ellipse at center, var(--gold-soft) 0%, var(--cream) 75%);
  }
  .contact {
    position: absolute;
    left: 0; top: 262px;
    width: 840px;
    margin: 0;
    text-align: center;
    color: var(--text);
    font-size: 32px;
    font-weight: 400;
    letter-spacing: -0.6px;
  }
  .contact p {
    margin: 0;
    height: 64px;
    line-height: 64px;
  }
  .contact .gap { display: inline-block; width: 40px; }
</style>
</head>
<body>
  <main class="card">
    <header class="header-band">
      <div class="brand-mark"></div>
      <p class="brand-name brand-name--primary">Hartwells</p>
      <p class="brand-name brand-name--echo" aria-hidden="true">Hartwells</p>
      <div class="scales-small" role="img" aria-label="Small scales of justice emblem"></div>
    </header>

    <div class="scales-large" role="img" aria-label="Large faint scales of justice decoration"></div>

    <address class="contact">
      <p>Dominic Hartwell Principal Hartwells Solicitors Pty Ltd</p>
      <p>Level 6, 47 Penrose Street Melbourne VIC Australia 3000</p>
      <p>T: +61 3 9555 0142<span class="gap"></span>F: +61 3 9555 0187</p>
      <p>E: dominic@hartwellsolicitors.com.au</p>
      <p>M:&nbsp; 0491 570 156</p>
    </address>

    <footer class="footer-band"></footer>
  </main>
</body>
</html>
```